Beacon Advisory Website

I currently have a website www.beaconadvisoryinc.example. We are a IT Consulting Company. Our website will pretty much tell out our services. I am looking to enhance my website and make it look more professional. Looking for very classy and Contemporary look and design for my website.

Industry/Entity Type

It Company

```html
<!DOCTYPE html>
<html lang="en">
<head>
<meta charset="utf-8">
<title>Beacon Advisory</title>
<link href="https://fonts.googleapis.com/css2?family=Oswald:wght@300;400;500&family=Open+Sans:wght@400;600&display=swap" rel="stylesheet">
<style>
:root{
  --blue:#1b5da8;
  --sky:#12a0dc;
  --teal:#15a39f;
  --ink:#333;
  --muted:#666;
  --white:#fff;
  --dark:#2e2620;
}
*{margin:0;padding:0;box-sizing:border-box}
html,body{width:676px;height:1200px;overflow:hidden;background:var(--white)}
body{position:relative;font-family:"Open Sans",sans-serif;color:var(--ink)}
.abs{position:absolute}
.head{font-family:"Oswald",sans-serif}

.topbar{left:0;top:0;width:676px;height:12px;background:var(--blue);color:var(--white);font-size:5.5px;line-height:12px}
.topbar .contact{left:142px;top:0}
.topbar .social{right:6px;top:2px;display:flex;gap:2px}
.sq{width:8px;height:8px;background:var(--white)}

.header{left:0;top:12px;width:676px;height:32px;background:var(--white)}
.brand{left:142px;top:7px;display:flex;align-items:center;gap:5px;font-family:"Oswald",sans-serif;font-weight:500;font-size:12px;color:var(--blue);letter-spacing:.5px}
.brand .mark{width:14px;height:14px;background:var(--blue)}
.nav{left:302px;top:2px;display:flex;font-family:"Oswald",sans-serif;font-size:6.4px;color:var(--blue);height:28px;align-items:center}
.nav span{padding:0 7px;line-height:28px}
.nav .active{background:var(--teal);color:var(--white);padding:0 4px}

.hero{left:0;top:44px;width:676px;height:200px;background:linear-gradient(90deg,#8c8a86 0%,#c9b9a8 30%,#6b5a4e 55%,#94897f 80%,#c8c4be 100%)}
.hero-title{left:302px;top:144px;width:374px;height:28px;background:var(--blue);color:var(--white);font-family:"Oswald",sans-serif;font-size:11px;line-height:28px;padding-left:5px}
.hero-box{left:0;top:174px;width:514px;height:44px;background:var(--sky)}
.hero-box p{position:absolute;left:306px;top:7px;width:200px;font-size:3.8px;line-height:4.6px;color:var(--white)}
.hero-box .more{position:absolute;left:306px;top:33px;font-size:3.6px;color:var(--white)}

.h2{font-family:"Oswald",sans-serif;font-weight:300;font-size:14px;color:#444}
.rule{height:2px;background:var(--teal)}

.about-text{left:140px;top:289px;width:222px;font-size:4.2px;line-height:5.4px;color:#555}
.pill{left:140px;top:324px;width:48px;height:11px;border-radius:6px;background:var(--teal);color:var(--white);font-family:"Oswald",sans-serif;font-size:5px;line-height:11px;padding-left:7px}
.pill i{position:absolute;right:2px;top:2px;width:7px;height:7px;border-radius:50%;background:var(--white)}
.photo{display:block}

.services-band{left:0;top:398px;width:676px;height:94px;background:var(--teal)}
.tabs{left:141px;top:414px;width:79px;background:var(--white);border-radius:2px;font-family:"Oswald",sans-serif;font-weight:300;font-size:5.4px;color:#555}
.tabs div{height:12.2px;line-height:12.2px;padding-left:4px;border-bottom:1px solid #ddd}
.tabs .current{color:var(--blue)}
.svc-title{left:242px;top:405px;color:var(--white);font-family:"Oswald",sans-serif;font-size:7px}
.svc-text{left:242px;top:419px;width:152px;color:var(--white);font-size:4.2px;line-height:5.2px}

.sub{left:140px;top:529px;color:var(--blue);font-size:6.4px}
.work-text{left:140px;top:547px;width:245px;font-size:4.2px;line-height:5.3px;color:#555}

.member{width:120px;text-align:center}
.member .ph{width:98px;height:98px;border-radius:50%;margin:0 auto;border:2px solid #e3e3e3}
.member .name{font-family:"Oswald",sans-serif;font-size:5.8px;color:var(--blue);margin-top:4px}
.member .role{font-size:3.8px;color:#777;margin-top:1px}

.panel{top:768px;height:154px;width:338px}
.panel h3{position:absolute;left:18px;top:84px;font-family:"Oswald",sans-serif;font-weight:400;font-size:22px;color:var(--white);letter-spacing:-.5px}
.panel p{position:absolute;left:18px;top:116px;width:250px;font-size:4.2px;line-height:5.2px;color:var(--white);text-transform:uppercase}

.contact-sec{left:0;top:922px;width:676px;height:206px;background:linear-gradient(100deg,#4a3a30 0%,#2c2520 45%,#3d3129 75%,#58493c 100%)}
.contact-title{left:0;top:944px;width:676px;text-align:center;font-family:"Oswald",sans-serif;font-size:13px;color:var(--white)}
.office{left:165px;width:90px;color:var(--white);font-size:4.3px;line-height:5.4px}
.office b{font-family:"Oswald",sans-serif;font-weight:400;font-size:5px;display:block}
.field{height:15px;border:1px solid #cfcfcf;background:rgba(255,255,255,.08);color:#ddd;font-size:5.2px;line-height:13px;padding-left:6px}
.submit{left:260px;top:1078px;width:243px;height:16px;background:var(--teal);color:var(--white);font-family:"Oswald",sans-serif;font-size:5.6px;line-height:16px;text-align:center}

.footer{left:0;top:1128px;width:676px;height:72px;background:var(--blue);color:var(--white);text-align:center}
.footer nav{position:absolute;left:0;top:10px;width:676px;font-family:"Oswald",sans-serif;font-size:6px}
.footer nav span{margin:0 3px}
.footer .social{position:absolute;left:320px;top:26px;display:flex;gap:2px}
.footer .copy{position:absolute;left:0;top:46px;width:676px;font-size:4.6px}
</style>
</head>
<body>

<div class="abs topbar">
  <div class="abs contact">&#9993; info@beaconadvisory.example &nbsp;|&nbsp; &#9742; +1 (555) 014 2290</div>
  <div class="abs social"><span class="sq"></span><span class="sq"></span><span class="sq"></span><span class="sq"></span></div>
</div>

<header class="abs header">
  <div class="abs brand"><span class="mark"></span>BEACON ADVISORY</div>
  <nav class="abs nav">
    <span class="active">Home</span><span>Company</span><span>Services</span><span>Solutions</span><span>Resources</span><span>Career</span><span>Contact Us</span>
  </nav>
</header>

<section>
  <div class="abs hero" role="img" aria-label="Smiling team of young professionals standing together"></div>
  <div class="abs hero-title">WELCOME TO BEACON ADVISORY</div>
  <div class="abs hero-box">
    <p>Effective integration of information technology into an organization's business processes has become increasingly crucial to prosperity. IT includes such items as the systems software, application software, computer hardware, networks and databases associated with managing an organization's information that quality falls by the wayside.</p>
    <span class="more">READ MORE &rarr;</span>
  </div>
</section>

<section>
  <h2 class="abs h2" style="left:140px;top:254px">About Us</h2>
  <div class="abs rule" style="left:140px;top:275px;width:56px"></div>
  <p class="abs about-text">Today's IT market is a dynamic, fast-paced industry, with ever-increasing demands. Meeting these demands for over 25 years, Beacon Advisory maintains a global presence, aggressively recruiting expertly qualified IT and Management Professionals from around the world and cultivating key partnerships with corporations to understand their business models end-to-end, with a goal of delivering exceptional client service and ensuring a consistent delivery of the talent needed to drive results.</p>
  <div class="abs pill">Read More<i></i></div>
  <div class="abs photo" style="left:370px;top:258px;width:165px;height:101px;background:linear-gradient(135deg,#b9c2b2,#e8e8e4 50%,#8d8478)" role="img" aria-label="Presenter at a whiteboard speaking to a seated team"></div>
</section>

<section>
  <h2 class="abs h2" style="left:140px;top:370px">Our Services</h2>
  <div class="abs rule" style="left:140px;top:391px;width:58px"></div>
  <div class="abs services-band"></div>
  <div class="abs tabs">
    <div class="current">Technology</div><div>Business</div><div>Application Developement</div><div>Enterprise Integration</div><div style="border:0">IT Consulting</div>
  </div>
  <div class="abs svc-title">Technology</div>
  <div class="abs svc-text">
    <p>Information technology should improve business results. Northfield helps companies make sure it does. We look at IT issues strategically, in the broader context of our clients' business. Our experts provide an objective, independent perspective to help companies realize the full potential of their IT resources, investments and assets.</p>
    <p style="margin-top:4px">We draw on global experience across industries and technologies to help solve companies' most complex IT challenges. More than 40% of</p>
  </div>
  <div class="abs photo" style="left:416px;top:405px;width:119px;height:79px;background:linear-gradient(135deg,#eef0f2,#c9ccd0 60%,#9aa0a6)" role="img" aria-label="Person pointing at a desktop monitor in an office"></div>
</section>

<section>
  <h2 class="abs h2" style="left:140px;top:503px">How We Work</h2>
  <div class="abs rule" style="left:140px;top:522px;width:80px"></div>
  <div class="abs sub">Beacon Advisory Advantage</div>
  <p class="abs work-text">We understand the complexities management faces when staffing a project. It isn't enough to simply supply a list of skilled and available candidates. Instead, we work hand in hand with you to provide a customized pool of talented professionals, uniquely qualified to make your project a success.</p>
  <div class="abs photo" style="left:394px;top:530px;width:141px;height:72px;background:linear-gradient(135deg,#3f6e66,#9fb7b2 55%,#d6dcdc)" role="img" aria-label="Video thumbnail of hands reviewing charts on a desk"></div>
  <svg class="abs" style="left:452px;top:554px" width="25" height="20" viewBox="0 0 25 20" aria-hidden="true">
    <rect width="25" height="20" rx="4" fill="#222" fill-opacity=".85"/>
    <path d="M10 5 L17 10 L10 15 Z" fill="#fff"/>
  </svg>
</section>

<section>
  <h2 class="abs h2" style="left:140px;top:613px">Our Team</h2>
  <div class="abs rule" style="left:140px;top:633px;width:58px"></div>
  <div class="abs member" style="left:137px;top:641px">
    <div class="ph" style="background:radial-gradient(circle at 50% 40%,#e6d2c2,#5c4c44 70%,#2d2d33)" role="img" aria-label="Portrait of Nora Whitfield"></div>
    <div class="name">nora whitfield</div><div class="role">CEO, Founding Partner</div>
  </div>
  <div class="abs member" style="left:278px;top:641px">
    <div class="ph" style="background:radial-gradient(circle at 50% 40%,#e2cbb8,#6d6e74 70%,#2a2c33)" role="img" aria-label="Portrait of Owen Carver"></div>
    <div class="name">owen carver</div><div class="role">Managing</div>
  </div>
  <div class="abs member" style="left:418px;top:641px">
    <div class="ph" style="background:radial-gradient(circle at 50% 40%,#ecd6c6,#4a4a50 70%,#222)" role="img" aria-label="Portrait of Milo Hartley"></div>
    <div class="name">Milo Hartley</div><div class="role">Founding Partner</div>
  </div>
</section>

<section>
  <div class="abs panel" style="left:0;background:linear-gradient(160deg,#6d7f93,#3e5f8a 55%,#2d5896)" role="img" aria-label="Businessman holding a smartphone in the city">
    <h3>ANYTIME. ANYWHERE.</h3>
    <p>Lorem ipsum is simply dummy text of the printing and typesetting industry. Lorem ipsum has been the industry's standard dummy text ever since the 1500s.</p>
  </div>
  <div class="abs panel" style="left:338px;background:linear-gradient(200deg,#9aaec2,#5a7fab 55%,#3563a0)" role="img" aria-label="Support agent wearing a headset">
    <h3>SUPPORT</h3>
    <p>Lorem ipsum is simply dummy text of the printing and typesetting industry. Lorem ipsum has been the industry's standard dummy text ever since the 1500s.</p>
  </div>
</section>

<section>
  <div class="abs contact-sec" role="img" aria-label="Person typing on a laptop beside a coffee cup"></div>
  <h2 class="abs contact-title">Contact Us</h2>

  <svg class="abs" style="left:165px;top:974px" width="4" height="6" viewBox="0 0 4 6" aria-hidden="true"><path d="M2 0a2 2 0 0 1 2 2c0 1.5-2 4-2 4S0 3.5 0 2a2 2 0 0 1 2-2z" fill="#fff"/></svg>
  <div class="abs office" style="top:981px"><b>HEAD OFFICE</b>480 HARBOR LANE<br>SUITE 310<br>WESTBROOK, NJ 07900<br>PHONE: +1 (555) 014 2290</div>
  <svg class="abs" style="left:165px;top:1019px" width="4" height="6" viewBox="0 0 4 6" aria-hidden="true"><path d="M2 0a2 2 0 0 1 2 2c0 1.5-2 4-2 4S0 3.5 0 2a2 2 0 0 1 2-2z" fill="#fff"/></svg>
  <div class="abs office" style="top:1026px"><b>TECHNICAL CENTER</b>2210 LINDEN PARKWAY<br>SUITE 140<br>RIDGEFIELD MI 48100</div>
  <svg class="abs" style="left:165px;top:1057px" width="5" height="5" viewBox="0 0 10 10" aria-hidden="true"><path d="M2 0l2 2-1 2c1 2 2 3 4 4l2-1 2 2-2 1C5 10 0 5 0 2z" fill="#fff"/></svg>
  <div class="abs office" style="top:1063px"><b>TALK WITH US</b>+1 (555) 014 2290</div>

  <div class="abs field" style="left:260px;top:975px;width:119px;color:#fff">First Name</div>
  <div class="abs field" style="left:385px;top:975px;width:118px">Last name</div>
  <div class="abs field" style="left:260px;top:999px;width:119px">Email</div>
  <div class="abs field" style="left:385px;top:999px;width:118px">Project name</div>
  <div class="abs field" style="left:260px;top:1021px;width:243px;height:50px;padding-top:2px">Your Message...</div>
  <div class="abs submit">SUBMIT</div>
</section>

<footer class="abs footer">
  <nav><span>Home</span><span>Company</span><span>Services</span><span>Solutions</span><span>Resources</span><span>Career</span><span>Contact Us</span></nav>
  <div class="social"><span class="sq"></span><span class="sq"></span><span class="sq"></span><span class="sq"></span></div>
  <div class="copy">Copyright @ Beacon Advisory</div>
</footer>

</body>
</html>
```